Covid 19 Exit Strategy one page brochure

I would like to design, and will need URGENT help, a brochure detailing a Covid 19 Exit Strategy plan. This brochure will need to be understood easily and the graphics inside should make it easy for people to understand without reading the entire text. This project is quite urgent and needs to be completed THIS WEEK - by Saturday may 16th at the latest. I am attaching two examples. I will provide the text.

```html
<!DOCTYPE html>
<html lang="en">
<head>
<meta charset="utf-8">
<title>Phased Covid-19 Lockdown Exit Strategy Plan</title>
<link rel="stylesheet" href="https://fonts.googleapis.com/css2?family=Poppins:wght@300;400&display=swap">
<style>
:root{
  --page:#07242a;
  --panel-a:#0d5a68;
  --panel-b:#157a8a;
  --panel-c:#0a3d48;
  --red-a:#c0141b;
  --red-b:#5a1e22;
  --text:#ffffff;
  --muted:#9aa3a6;
}
*{margin:0;padding:0;box-sizing:border-box}
html,body{width:1200px;height:5051px;overflow:hidden}
body{background:var(--page);font-family:'Poppins',sans-serif;color:var(--text);position:relative}
.title{position:absolute;left:27px;top:68px;font-weight:400;font-size:41px;letter-spacing:.2px;white-space:nowrap}
.title .accent{color:var(--muted)}
.stage{position:absolute;left:27px;width:1146px;
  background:radial-gradient(ellipse at 65% 40%,var(--panel-b) 0%,var(--panel-a) 45%,var(--panel-c) 100%);}
.stage-1{top:176px;height:1671px}
.stage-2{top:1898px;height:1714px}
.stage-3{top:3663px;height:1369px}
.stage-tab{position:absolute;left:12px;width:212px;top:36px;
  background:linear-gradient(180deg,var(--red-a) 0%,#8e1a20 35%,var(--red-b) 100%);
  text-align:center;padding-top:14px}
.stage-1 .stage-tab{height:749px}
.stage-2 .stage-tab{height:945px}
.stage-3 .stage-tab{height:1024px}
.stage-name,.stage-num{font-size:59px;line-height:70px;font-weight:400}
.stage-rule{font-size:19px;line-height:36.5px;text-transform:uppercase;font-weight:300;padding:8px 16px 0;width:212px;margin:0 auto}
.item{position:absolute;left:248px;width:900px}
.item svg{position:absolute;left:0;top:-6px;width:44px;height:44px}
.item p{margin-left:74px;font-size:17px;line-height:21.5px;font-weight:300;width:772px}
</style>
</head>
<body>
<svg width="0" height="0" style="position:absolute" aria-hidden="true">
 <defs>
  <g id="i-elder" fill="none" stroke="#fff" stroke-width="2.2"><circle cx="20" cy="28" r="10"/><circle cx="20" cy="28" r="3"/><path d="M8 10h10l4 10M30 6v14h8"/><circle cx="36" cy="36" r="3"/></g>
  <g id="i-group" fill="none" stroke="#fff" stroke-width="2"><path d="M10 18a12 8 0 0 1 24 0a6 6 0 0 1-24 0"/><circle cx="10" cy="32" r="4"/><circle cx="22" cy="32" r="4"/><circle cx="34" cy="32" r="4"/><path d="M4 42h36"/></g>
  <g id="i-hand" fill="none" stroke="#fff" stroke-width="2"><rect x="22" y="6" width="16" height="12" rx="3"/><path d="M8 38v-12l6-6l8 8v10M6 42h18"/></g>
  <g id="i-virus" fill="none" stroke="#fff" stroke-width="2"><circle cx="22" cy="22" r="10"/><path d="M22 4v8M22 32v8M4 22h8M32 22h8M9 9l6 6M29 29l6 6M35 9l-6 6M9 35l6-6"/></g>
  <g id="i-car" fill="none" stroke="#fff" stroke-width="2"><path d="M3 26l6-8h20l8 6h5v6H3z"/><circle cx="12" cy="31" r="3"/><circle cx="34" cy="31" r="3"/></g>
  <g id="i-heart" fill="none" stroke="#4fd1e0" stroke-width="3"><path d="M22 38L6 22a8 8 0 0 1 16-8a8 8 0 0 1 16 8z"/><path d="M8 22h8l3-5l4 9l3-4h10"/></g>
  <g id="i-tower" fill="none" stroke="#fff" stroke-width="2"><rect x="12" y="6" width="22" height="34"/><rect x="4" y="20" width="8" height="20"/><path d="M17 12h4M25 12h4M17 19h4M25 19h4M17 26h4M25 26h4M17 33h4M25 33h4"/></g>
  <g id="i-staff" fill="none" stroke="#fff" stroke-width="2"><circle cx="22" cy="14" r="8"/><path d="M8 40a14 12 0 0 1 28 0M14 22l-6 6M30 22l6 6"/></g>
  <g id="i-shop" fill="none" stroke="#fff" stroke-width="2"><path d="M4 10h36l-3 8H7zM7 18v22h30V18M16 40V28h12v12"/></g>
  <g id="i-pharm"><rect x="6" y="6" width="32" height="32" fill="#fff"/><rect x="9" y="9" width="26" height="26" fill="#1a85b0"/><path d="M22 13v18M14 22h16M16 16l12 12M28 16L16 28" stroke="#fff" stroke-width="2.5"/></g>
  <g id="i-bus" fill="none" stroke="#fff" stroke-width="2"><rect x="4" y="8" width="36" height="24" rx="3"/><path d="M4 18h36M10 8v10M18 8v10M26 8v10M34 8v10"/><circle cx="12" cy="35" r="3"/><circle cx="32" cy="35" r="3"/></g>
  <g id="i-pray" fill="none" stroke="#fff" stroke-width="2"><path d="M22 40V14l-4-8l-10 24l6 10M22 14l4-8l10 24l-6 10"/></g>
  <g id="i-museum" fill="none" stroke="#fff" stroke-width="2"><circle cx="22" cy="22" r="18"/><path d="M12 18l10-6l10 6zM14 20v10M20 20v10M24 20v10M30 20v10M11 32h22"/></g>
  <g id="i-coffee" fill="none" stroke="#fff" stroke-width="2"><path d="M6 24h20v12a4 4 0 0 1-4 4H10a4 4 0 0 1-4-4zM26 28h5a3 3 0 0 1 0 6h-5M12 18c0-4 4-4 4-8M30 20l8-10v18"/></g>
  <g id="i-school" fill="none" stroke="#fff" stroke-width="2"><path d="M6 40V18l16-10l16 10v22zM16 40V30h12v10M18 20h8"/></g>
  <g id="i-cinema" fill="none" stroke="#fff" stroke-width="2"><rect x="6" y="8" width="32" height="30"/><path d="M6 14h32M10 8v6M16 8v6M22 8v6M28 8v6M34 8v6M16 38V26h12v12"/></g>
 </defs>
</svg>

<h1 class="title">PHASED <span class="accent">COVID-19</span> LOCKDOWN EXIT STRATEGY PLAN</h1>

<section class="stage stage-1">
 <div class="stage-tab"><div class="stage-name">STAGE</div><div class="stage-num">1</div>
  <p class="stage-rule">To enter this stage, additional to the general requirements, the effective reproduction number (Rt) must be less than 1 and the death rate at less than 3%. The economy and social activities can resume in this sequence:</p></div>
</section>
<section class="stage stage-2">
 <div class="stage-tab"><div class="stage-name">STAGE</div><div class="stage-num">2</div>
  <p class="stage-rule">To enter stage 2 of the Covid-19 exit strategy, compliance to the general requirements is compulsory, additional to a successful stage 1 outcome. The effective reproduction number (Rt) for stage 2 must be less than 0.5 and the death rate stabilized at less than 1.5%. The economy and social activities can resume in this sequence:</p></div>
</section>
<section class="stage stage-3">
 <div class="stage-tab"><div class="stage-name">STAGE</div><div class="stage-num">3</div>
  <p class="stage-rule">To enter stage 3 of the Covid-19 exit strategy, compliance to the general re-quirements is compulsory, additional to a successful stage 2 out-come. The effective re-production number (Rt) for stage 3 must be less than 0.3 and the death rate stabilized at less than 1%. The economy and social activities can resume in this sequence:</p></div>
</section>

<!-- Stage 1 measures -->
<div class="item" style="top:239px"><svg viewBox="0 0 44 44"><use href="#i-elder"/></svg><p>Elderly (60+ years old) and vulnerable individuals should continue to self-isolate.</p></div>
<div class="item" style="top:325px"><svg viewBox="0 0 44 44"><use href="#i-group"/></svg><p>No more than 5 people maximum gathering at a time in public areas and at work.</p></div>
<div class="item" style="top:418px"><svg viewBox="0 0 44 44"><use href="#i-hand"/></svg><p>Work from home should continue whenever and as much as possible.</p></div>
<div class="item" style="top:496px"><svg viewBox="0 0 44 44"><use href="#i-virus"/></svg><p>Social distancing should continue to be re-enforced in public areas, at work and in all areas reopened.</p></div>
<div class="item" style="top:584px"><svg viewBox="0 0 44 44"><use href="#i-car"/></svg><p>Non-essential travel should be minimized between cities and regions<br>(and within cities and regions where covid-19 infections are still a risk)</p></div>
<div class="item" style="top:676px"><svg viewBox="0 0 44 44"><use href="#i-tower"/></svg><p>Large businesses (300 people and more, manufacturing, services, etc.) can reopen progressively. Common areas should remain closed (cafeteria, restaurant, gym, meeting rooms of no more than 5 people).</p></div>
<div class="item" style="top:786px"><svg viewBox="0 0 44 44"><use href="#i-staff"/></svg><p>Small businesses (300 people and less) can reopen as well with the same conditions as large businesses.</p></div>
<div class="item" style="top:866px"><svg viewBox="0 0 44 44"><use href="#i-shop"/></svg><p>Commercial shops can reopen. Shops should control the flow of people in their facilities not to exceed 30% at a time of standard capacity. Shops should provide disinfectant and temperature control at entry.</p></div>
<div class="item" style="top:959px"><svg viewBox="0 0 44 44"><use href="#i-pharm"/></svg><p>Pharmacies will continue to be open. However, they must make available disinfectant for use by clients and will continue to comply with social distancing. Pharmacies should limit the number of client/patient in their stores not to exceed 30% of the standard capacity.</p></div>
<div class="item" style="top:1072px"><svg viewBox="0 0 44 44"><use href="#i-bus"/></svg><p>Transportation (buses, taxis, airlines) will resume progressively. No air travels permitted in and out of Covid-19 known hotspots, locally or internationally. Entry to country should be limited and strictly controlled. All landing passengers and visitors regardless of the country of origin should be tested for Covid-19 at arrival. All passengers and visitors will undergo a temperature check at arrival. No more than 3 people at a time in a taxi/Ridely including the driver. All passengers wearing masks. Buses should operate with no more than 30% customer's capacity per bus.</p></div>
<div class="item" style="top:1268px"><svg viewBox="0 0 44 44"><use href="#i-pray"/></svg><p>Religious sites can reopen with a maximum capacity of 30% or less. Social distancing and wearing masks is mandatory. Religious sites should organize (volunteers can help) to check body temperature of everyone accessing the site and provide disinfectant at entry.</p></div>
<div class="item" style="top:1386px"><svg viewBox="0 0 44 44"><use href="#i-museum"/></svg><p>Hotels &amp; tourism (museums, etc.) can reopen but must operate at 30% or less capacity. All common areas (restaurants, gyms, swimming pools, conference rooms, etc.) should remain closed.</p></div>
<div class="item" style="top:1478px"><svg viewBox="0 0 44 44"><use href="#i-coffee"/></svg><p>Coffee &amp; restaurants can reopen but must operate at 30% capacity as well and comply with social distancing. Clients must wear as much as possible their masks if they are not consuming food/coffee. Clients should avoid to talking to each other with masks off.</p></div>
<div class="item" style="top:1592px"><svg viewBox="0 0 44 44"><use href="#i-school"/></svg><p>All schools should remain closed. On-line courses should continue be the preferred method for education.</p></div>
<div class="item" style="top:1688px"><svg viewBox="0 0 44 44"><use href="#i-cinema"/></svg><p>Large scale events (cinema, theaters, sport, business conferences, etc.) should remain closed or operate virtually. Sport events can resume but without spectators. Athletes and the staff surrounding them should be tested, disinfectants should be available and masks used as much as reasonably possible.</p></div>

<!-- Stage 2 measures -->
<div class="item" style="top:1935px"><svg viewBox="0 0 44 44"><use href="#i-elder"/></svg><p>Elderly (60+ years old) and vulnerable individuals should continue to self-isolate as much as possible.</p></div>
<div class="item" style="top:2019px"><svg viewBox="0 0 44 44"><use href="#i-group"/></svg><p>No more than 10 people maximum gathering at a time in public areas and at work.</p></div>
<div class="item" style="top:2106px"><svg viewBox="0 0 44 44"><use href="#i-hand"/></svg><p>Work from home should if possible or for jobs that do not have to be necessarily in an office setup.</p></div>
<div class="item" style="top:2202px"><svg viewBox="0 0 44 44"><use href="#i-virus"/></svg><p>Social distancing can be relaxed. However people should continue to wear masks and use disinfectants.</p></div>
<div class="item" style="top:2288px"><svg viewBox="0 0 44 44"><use href="#i-car"/></svg><p>Travel can resume between cities and regions. The same containment restrictions should apply to any existing hotspot.</p></div>
<div class="item" style="top:2374px"><svg viewBox="0 0 44 44"><use href="#i-heart"/></svg><p>Elective surgeries can resume in hospitals and clinics that are equipped to comply with all general requirements.</p></div>
<div class="item" style="top:2455px"><svg viewBox="0 0 44 44"><use href="#i-tower"/></svg><p>Large businesses (300 people and more, manufacturing, services, etc.) will continue to operate. Common areas should open but social distancing should remain (cafeteria, restaurant, gym, meeting rooms of no more than 10 people).</p></div>
<div class="item" style="top:2561px"><svg viewBox="0 0 44 44"><use href="#i-staff"/></svg><p>Small businesses (300 people and less) will continue to operate with the same conditions as large businesses.</p></div>
<div class="item" style="top:2643px"><svg viewBox="0 0 44 44"><use href="#i-shop"/></svg><p>Commercial shops will continue to be open and can operate at 50% capacity. Wear of masks should continue.</p></div>
<div class="item" style="top:2747px"><svg viewBox="0 0 44 44"><use href="#i-pharm"/></svg><p>Pharmacies will continue to be open and will need to operate a 50% capacity</p></div>
<div class="item" style="top:2841px"><svg viewBox="0 0 44 44"><use href="#i-bus"/></svg><p>Transportation (buses, taxis, and airlines) will continue to operate. Still no air travels permitted in and out of Covid-19 known hotspots, locally or internationally. Entry to country should be relaxed but remain controlled. Airports should continue to use thermo cameras to monitor passenger's temperature at landing. Airports should be equipped to test for Covid-19 if necessary. Transportation by taxi/Ridely continues, however, passengers wear masks. Buses could operate with 50% capacity per bus.</p></div>
<div class="item" style="top:3045px"><svg viewBox="0 0 44 44"><use href="#i-pray"/></svg><p>Religious sites can operate with a maximum capacity of 50%. Social distancing and wearing masks should be enforced. Sites should continue to check body temperature of everyone accessing the site and provide disinfectant at entry.</p></div>
<div class="item" style="top:3167px"><svg viewBox="0 0 44 44"><use href="#i-museum"/></svg><p>Hotels &amp; tourism (museums, etc.) can operate at 50% capacity. All common areas (restaurants, gyms, swimming pools, conference rooms, etc.) could reopen. Gatherings are limited to 10 people or less and can be expanded with social distancing and wearing protective masks.</p></div>
<div class="item" style="top:3284px"><svg viewBox="0 0 44 44"><use href="#i-coffee"/></svg><p>Coffee &amp; restaurants can operate at 50% capacity and continue comply with social distancing. Clients must wear as much as possible their masks if they are not consuming food/coffee.</p></div>
<div class="item" style="top:3402px"><svg viewBox="0 0 44 44"><use href="#i-school"/></svg><p>Schools can reopen in parallel with on-line education. Social distancing and re-arranging school seating to prevent the spread of infection is mandatory.</p></div>
<div class="item" style="top:3496px"><svg viewBox="0 0 44 44"><use href="#i-cinema"/></svg><p>Large scale events (cinema, theaters, sport, business conferences, etc.) could resume under strict social distancing. People should wear masks.</p></div>

<!-- Stage 3 measures -->
<div class="item" style="top:3700px"><svg viewBox="0 0 44 44"><use href="#i-elder"/></svg><p>Elderly (60+ years old) and vulnerable individuals may resume all previously exercised activities without restrictions.</p></div>
<div class="item" style="top:3784px"><svg viewBox="0 0 44 44"><use href="#i-group"/></svg><p>Restrictions as to the number of people gathering together can be lifted. Social distancing can be relaxed. However, wear of masks may continue.</p></div>
<div class="item" style="top:3865px"><svg viewBox="0 0 44 44"><use href="#i-car"/></svg><p>Travel can resume between cities and regions and out of country travel. The same containment restrictions as Stage 1 and 2 would continue to apply to any existing hotspot.</p></div>
<div class="item" style="top:3969px"><svg viewBox="0 0 44 44"><use href="#i-heart"/></svg><p>All hospital and clinic surgeries can resume in hospitals in compliance with standard hospital and health care procedures.</p></div>
<div class="item" style="top:4055px"><svg viewBox="0 0 44 44"><use href="#i-tower"/></svg><p>Large businesses (300 people and more, manufacturing, services, etc.) will resume normal business practices. Wear of masks is recommended but not mandatory.</p></div>
<div class="item" style="top:4145px"><svg viewBox="0 0 44 44"><use href="#i-staff"/></svg><p>Small businesses (300 people and less) will operate with the same conditions as large businesses.</p></div>
<div class="item" style="top:4245px"><svg viewBox="0 0 44 44"><use href="#i-shop"/></svg><p>Commercial shops can operate on a normal mode - previous to covid19. Wear of masks could be recommended in certain areas.</p></div>
<div class="item" style="top:4337px"><svg viewBox="0 0 44 44"><use href="#i-pharm"/></svg><p>Pharmacies can operate at a normal state.</p></div>
<div class="item" style="top:4427px"><svg viewBox="0 0 44 44"><use href="#i-bus"/></svg><p>Transportation (buses, taxis, and airlines) will operate at a normal capacity. Still no air travels permitted in and out of Covid-19 known hotspots, locally or internationally. Entry to country should be relaxed and operate normally. Airports should continue to use thermo cameras to monitor passenger's temperature at landing. Airports should be equipped to test for Covid-19 if necessary. Transportation by taxi / Ridely and buses will resume on a normal mode. Wear of masks is elective.</p></div>
<div class="item" style="top:4608px"><svg viewBox="0 0 44 44"><use href="#i-pray"/></svg><p>Religious sites can operate normally. Wear of masks should be elective.</p></div>
<div class="item" style="top:4686px"><svg viewBox="0 0 44 44"><use href="#i-museum"/></svg><p>Hotels &amp; tourism (museums, etc.) can operate at 100% capacity including all common areas</p></div>
<div class="item" style="top:4788px"><svg viewBox="0 0 44 44"><use href="#i-coffee"/></svg><p>Coffee &amp; restaurants can resume normal operations. Clients may wear masks for personal protection if they wish to.</p></div>
<div class="item" style="top:4878px"><svg viewBox="0 0 44 44"><use href="#i-school"/></svg><p>Schools can resume operations. Re-arranging school seating should continue until a vaccine is found.</p></div>
</body>
</html>
```